Reef Glow

sunglasses, sihoullette of body, maybe wearing a bikini or sunglasses. I am offering spray tanning, body wraps, tanning beds, stand up, body art, airbrush makeup.

Target Market(s)

I would say my target is all ages, But tanning is a seasonal business and more beauty and aging concept. and around prom time I get my most profitable business. so 18 to 21 through march and april. then 25 to 55 through april to june.

Industry/Entity Type

Makeup

Contact Information for Business Card

Phone number: 701-382-5147 Owner: Jan Mortby (Lisowski)

Colors

Designer to choose colors to be used in the design.

Requirements
Nice to have
• Sunglasses, silouttes of body wearing sunglasses or bikini, or picture of spray gun.

```html
<!DOCTYPE html>
<html lang="en">
<head>
<meta charset="utf-8">
<title>Jan Mortby — Business Cards</title>
<link href="https://fonts.googleapis.com/css2?family=Lato:wght@400;700&display=swap" rel="stylesheet">
<style>
  :root {
    --page: #ededed;
    --sun: #fbee3a;
    --ink: #161408;
    --rule-dark: #6b6840;
    --rule-light: #8a8a3a;
  }
  * { margin: 0; padding: 0; box-sizing: border-box; }
  html, body {
    width: 1200px;
    height: 900px;
    overflow: hidden;
    background: var(--page);
    font-family: "Lato", "Carlito", Arial, sans-serif;
  }
  .card {
    position: absolute;
    left: 374px;
    width: 514px;
    height: 297px;
  }
  .card--light { top: 131px; background: var(--sun); color: var(--ink); }
  .card--dark  { top: 479px; background: var(--ink); color: var(--sun); }

  .brand {
    position: absolute;
    left: 30px;
    top: 96px;
    display: flex;
    align-items: center;
    gap: 12px;
  }
  .brand__dot {
    width: 22px;
    height: 22px;
    border-radius: 50%;
    background: currentColor;
  }
  .brand__name {
    font-size: 40px;
    font-weight: 700;
    line-height: 1;
    letter-spacing: 0.5px;
  }
  .phone {
    position: absolute;
    left: 64px;
    top: 152px;
    font-size: 15px;
    font-weight: 400;
  }
  .divider {
    position: absolute;
    left: 344px;
    top: 26px;
    width: 1px;
    height: 228px;
  }
  .card--light .divider { background: var(--rule-light); }
  .card--dark  .divider { background: var(--rule-dark); }

  .services {
    position: absolute;
    left: 364px;
    top: 97px;
    list-style: none;
    font-size: 11px;
    line-height: 16px;
  }
  .services__lead {
    font-size: 14px;
    font-weight: 700;
  }
</style>
</head>
<body>

  <section class="card card--light">
    <div class="brand">
      <span class="brand__dot"></span>
      <span class="brand__name">Jan Mortby</span>
    </div>
    <p class="phone">701-382-5147</p>
    <div class="divider"></div>
    <ul class="services">
      <li><span class="services__lead">S</span>pray tanning.</li>
      <li>Body wraps.</li>
      <li>Tanning beds.</li>
      <li>Stand up.</li>
      <li>Body art.</li>
      <li>Airbrush makeup.</li>
    </ul>
  </section>

  <section class="card card--dark">
    <div class="brand">
      <span class="brand__dot"></span>
      <span class="brand__name">Jan Mortby</span>
    </div>
    <p class="phone">701-382-5147</p>
    <div class="divider"></div>
    <ul class="services">
      <li><span class="services__lead">S</span>pray tanning.</li>
      <li>Body wraps.</li>
      <li>Tanning beds.</li>
      <li>Stand up.</li>
      <li>Body art.</li>
      <li>Airbrush makeup.</li>
    </ul>
  </section>

</body>
</html>
```